Webdesign for Dutch IT consultancy company

Make a Wordpress webdesign for a Dutch consultancy company

Briefing Brivola IT

Website for finding and connecting IT-professionals. Corebusiness is to find IT-professionals and to help them to follow their ambitions. We offer training, personal coaching and education trajects.

U can take www.Tavemko.nl as an example for the website.

Home page

U can take www.Tavemko.nl as an example.

There should be jobs on the home page. A block for short info about us and about what whe do and a trigger to contact us quickly.

Jobs Page

On this page should be the jobs that we offer for the professionals. There should be a search function on this page so u can easily find the job that you are looking for.

A call to action can be on this page too.

Also a little block with text for some information.

For professionals page

Block with information on top. Call to action. info about who we work for/with.

For Clients

Info about three different solutions

- Sourcing solutions
- Consultancy solutions
- Custom based traineeships

Request a qoute option

Traineeships page

Info about two different traineeships

- Linux traineeships
- Microsoft traineeships

Call to action/ subscribe for traineeships

About us page

We are BrivolaT IT

Our mission: Creating cooperations between young professionals and businesses who wanna work on a great future.

Our core values

Last news

Target Market(s)

Young professionals and businesses who need IT services

Industry/Entity Type

It Company

Coding

Coded - Design and coding required

Number of Pages Required

5+ page

Font styles to use
Other font styles liked:
• Calibri

Colors
ffffff
add136
6b449b

Requirements
Must have
• Home page, Jobs Page, Professionals page, Clients page, Traineeships page, About us Page
• Green and/or Purple layout. Job search option, subscribe option
Nice to have
• modern design

```html
<!DOCTYPE html>
<html lang="en">
<head>
<meta charset="utf-8">
<title>Brivola IT – Sourcing and Consultancy</title>
<link href="https://fonts.googleapis.com/css2?family=Open+Sans:wght@400;600;700&display=swap" rel="stylesheet">
<style>
:root{
  --green:#8bc53f;
  --green-dark:#6fa52b;
  --purple:#6b449b;
  --ink:#1c1c1c;
  --text:#555;
  --muted:#888;
  --line:#e2e2e2;
  --dark:#2a2a2a;
  --darker:#1b1b1b;
  --white:#fff;
}
*{box-sizing:border-box;margin:0;padding:0}
html,body{width:1200px;height:3455px;overflow:hidden}
body{font-family:"Open Sans",Arial,sans-serif;color:var(--text);background:var(--white);position:relative}
.sec{position:absolute;left:0;width:1200px}
.topbar{top:0;height:28px;background:var(--darker);color:#eee;font-size:11px;font-weight:600;display:flex;justify-content:space-between;align-items:center;padding:0 60px}
.header{top:28px;height:103px}
.brand{position:absolute;left:60px;top:30px;display:flex;align-items:center;gap:10px;font-size:38px;font-weight:700;color:var(--purple);letter-spacing:1px}
.brand i{width:26px;height:26px;background:var(--purple);display:block}
.contact{position:absolute;top:30px;display:flex;gap:14px;align-items:flex-start}
.contact .ico{width:40px;height:40px;border-radius:50%;background:#eef6e3;display:flex;align-items:center;justify-content:center}
.contact b{display:block;font-size:12px;color:var(--ink);font-weight:600;margin-top:2px}
.contact span{font-size:12px;color:var(--muted)}
.nav{top:131px;left:60px;width:1078px;height:49px;background:var(--green);display:flex;align-items:center}
.nav a{color:var(--white);font-size:12.5px;font-weight:700;text-decoration:none;padding:0 16px;height:49px;line-height:49px}
.nav a.active{background:var(--green-dark)}
.nav .search{margin-left:auto;width:56px;display:flex;justify-content:center;align-items:center}
.nav .quote{background:var(--green-dark);width:160px;text-align:center;padding:0}
.hero{top:180px;height:545px;background:linear-gradient(120deg,#cfd2d6 0%,#a9aeb4 40%,#d9dcdf 70%,#8e949b 100%)}
.hero .band{position:absolute;left:288px;top:200px;width:624px;height:140px;background:rgba(255,255,255,.55)}
.hero h1{position:absolute;left:0;top:208px;width:1200px;text-align:center;font-size:36px;font-weight:600;color:#111;line-height:50px}
.about{top:725px;height:525px}
.about .photo{position:absolute;left:60px;top:76px;width:481px;height:360px;background:linear-gradient(135deg,#7a6e66,#c9c1b8 50%,#5a524d)}
.about h2{position:absolute;left:599px;top:80px;font-size:30px;font-weight:600;color:var(--ink)}
.about h2 em{font-style:normal;color:var(--purple)}
.about p{position:absolute;left:599px;top:146px;width:545px;font-size:13px;line-height:29px;color:var(--muted)}
.stat{position:absolute;top:295px;width:200px;text-align:center}
.stat .ring{width:78px;height:78px;border-radius:50%;background:var(--white);box-shadow:0 3px 8px rgba(0,0,0,.3);margin:0 auto;display:flex;align-items:center;justify-content:center}
.stat strong{display:block;font-size:30px;font-weight:700;color:var(--purple);margin-top:14px;line-height:36px}
.stat span{font-size:12px;color:var(--ink)}
.services{top:1250px;height:549px;background:linear-gradient(90deg,#e4e6e9,#d3d6da 50%,#e6e7e9)}
.services h2{position:absolute;left:60px;top:52px;font-size:42px;font-weight:600;color:var(--ink)}
.services .intro{position:absolute;left:362px;top:50px;width:790px;font-size:16px;line-height:23px;color:var(--ink)}
.diagram{position:absolute;left:0;top:0}
.svc-logo{position:absolute;left:0;top:170px;width:1200px;text-align:center;font-size:34px;font-weight:700;color:var(--purple)}
.svc{position:absolute;font-size:20px;color:var(--ink);line-height:26px}
.jobs{top:1799px;height:612px}
.jobs h2,.faq h2{position:absolute;top:78px;font-size:30px;font-weight:600;color:var(--ink)}
.card{position:absolute;top:138px;width:244px}
.card .img{height:161px;position:relative}
.card .date{position:absolute;left:18px;top:16px;width:53px;height:62px;background:var(--green);color:var(--white);text-align:center;font-size:12px;line-height:28px}
.card .date b{display:block;background:#6fa52b;font-size:17px;font-weight:600;line-height:34px}
.card h3{font-size:16px;font-weight:600;color:var(--purple);margin-top:30px}
.card .meta{font-size:12px;color:var(--ink);margin-top:12px;display:flex;gap:18px;align-items:center}
.card p{font-size:13px;line-height:20px;color:var(--ink);margin-top:8px}
.card .more{font-size:12px;font-weight:600;color:var(--ink);margin-top:24px;display:block}
.faq{position:absolute;left:663px;width:477px;top:0;height:612px}
.faq h2{left:0}
.faq ul{position:absolute;top:138px;left:0;width:477px;list-style:none;border-top:1px solid var(--line)}
.faq li{height:57px;border-bottom:1px solid var(--line);display:flex;align-items:center;font-size:14px;font-weight:600;color:var(--ink);padding-left:6px}
.faq li b{color:var(--purple);font-size:22px;font-weight:400;margin-right:14px}
.consult{top:2411px;height:456px}
.consult .img{position:absolute;left:0;top:0;width:580px;height:456px;background:linear-gradient(135deg,#6d6a66,#b7b3ad 50%,#4f4c48)}
.adviser{position:absolute;left:60px;top:118px;width:440px;height:246px;background:rgba(255,255,255,.78);padding:26px 28px}
.adviser h2{font-size:30px;font-weight:600;color:var(--ink)}
.adviser p{font-size:13px;line-height:21px;color:var(--ink);margin-top:10px}
.adviser .hours{font-size:13px;line-height:22px;color:var(--ink);margin-top:6px;font-weight:600}
.form{position:absolute;left:580px;top:0;width:620px;height:456px;background:#161616}
.form h2{position:absolute;left:57px;top:56px;font-size:30px;font-weight:600;color:var(--white)}
.field{position:absolute;border:1px solid #444;background:#121212;color:#aaa;font-size:13px;padding:9px 10px}
.btn{position:absolute;left:63px;top:332px;width:497px;height:41px;background:var(--purple);color:var(--white);font-size:13px;font-weight:600;text-align:center;line-height:41px}
.partners{top:2867px;height:168px;display:flex;align-items:center;justify-content:space-between;padding:0 60px}
.partners span{font-size:28px;font-weight:700;color:#555;display:flex;align-items:center;gap:10px}
.partners i{width:18px;height:18px;border-radius:50%;background:#555;display:block}
.footer{top:3035px;height:369px;background:var(--dark);color:#aaa}
.footer .col{position:absolute;top:64px}
.footer h4{font-size:20px;font-weight:600;color:var(--white);margin-top:6px}
.footer .brandf{font-size:30px;font-weight:700;color:#bbb;margin-top:0}
.footer p{font-size:13px;line-height:22px;color:#aaa}
.footer ul{list-style:none;margin-top:14px}
.footer li{font-size:12.5px;line-height:31px;color:#aaa}
.footer li::before{content:"‹ ";color:#777}
.socials{display:flex;gap:12px;margin-top:24px}
.socials i{width:36px;height:36px;border-radius:50%;background:#1e9a4a;display:block}
.socials.plain i{width:14px;height:14px;background:#888}
.news{display:flex;gap:14px;margin-top:26px}
.news .thumb{width:75px;height:40px}
.news span{font-size:13px;line-height:18px;color:#ddd}
.sub{display:flex;margin-top:20px}
.sub div{width:220px;height:38px;background:#1e1e1e}
.sub b{width:38px;height:38px;background:var(--green);display:flex;align-items:center;justify-content:center}
.bottom{top:3404px;height:51px;background:var(--darker);color:#aaa;font-size:11px;display:flex;align-items:center;padding:0 60px}
.bottom nav{margin-left:auto;display:flex;gap:70px;font-weight:600;color:#ccc;font-size:10px}
</style>
</head>
<body>

<div class="sec topbar"><span>Welcome to Sourcing and Consultancy</span><span>Monday - friday : 8:00 AM to 7:00 PM</span></div>

<header class="sec header">
  <div class="brand"><i></i>Brivola IT</div>
  <div class="contact" style="left:477px">
    <div class="ico"><svg width="18" height="18" viewBox="0 0 24 24"><path d="M3 11l9-7 9 7v9h-6v-6H9v6H3z" fill="#8bc53f"/></svg></div>
    <div><b>48, Kade Lane</b><span>Harlow, NL 2011</span></div>
  </div>
  <div class="contact" style="left:700px">
    <div class="ico"><svg width="18" height="18" viewBox="0 0 24 24"><path d="M6 3l4 4-2 3c1 2 3 4 6 6l3-2 4 4-3 3C10 21 3 14 3 6z" fill="#8bc53f"/></svg></div>
    <div><b>Call Us On</b><span>1-555-014-2290</span></div>
  </div>
  <div class="contact" style="left:918px">
    <div class="ico"><svg width="18" height="18" viewBox="0 0 24 24"><rect x="3" y="6" width="18" height="12" fill="#8bc53f"/><path d="M3 6l9 7 9-7" stroke="#fff" stroke-width="1.5" fill="none"/></svg></div>
    <div><b>Mail Us @</b><span>hello@brivolait.example</span></div>
  </div>
</header>

<nav class="sec nav">
  <a class="active">HOME</a><a>ABOUT US</a><a>SERVICES</a><a>PROJECTS</a><a>LATEST NEWS</a><a>PRODUCTS</a><a>MY ACCOUNT</a><a>CONTACT US</a>
  <a class="search"><svg width="16" height="16" viewBox="0 0 24 24"><circle cx="10" cy="10" r="7" stroke="#fff" stroke-width="3" fill="none"/><path d="M15 15l6 6" stroke="#fff" stroke-width="3"/></svg></a>
  <a class="quote">GET A QUOTE</a>
</nav>

<section class="sec hero" role="img" aria-label="Photo of a business team meeting around a presenter at a whiteboard">
  <div class="band"></div>
  <h1>Providing best business solution for<br>growing your business</h1>
</section>

<section class="sec about">
  <div class="photo" role="img" aria-label="Photo of colleagues working together around a table"></div>
  <h2>About our <em>Sourcing and Consultancy</em></h2>
  <p>We help IT professionals grow step by step. We travel the road with them and back again. Our advice is honest and our coaches are partners you can trust. It's time to learn new skills. It's time to aim higher. Our whole team works together and does it our way. There's no challenge we avoid. We believe every goal is possible. Together there's no stopping us.</p>
  <div class="stat" style="left:552px"><div class="ring"><svg width="34" height="34" viewBox="0 0 24 24"><circle cx="12" cy="8" r="4" stroke="#333" stroke-width="1.5" fill="none"/><path d="M4 21c0-5 4-7 8-7s8 2 8 7" stroke="#333" stroke-width="1.5" fill="none"/></svg></div><strong>2456+</strong><span>Engineers &amp; Workers</span></div>
  <div class="stat" style="left:761px"><div class="ring"><svg width="34" height="34" viewBox="0 0 24 24"><rect x="6" y="3" width="12" height="18" rx="1" stroke="#333" stroke-width="1.5" fill="none"/><path d="M9 7h6M9 11h6M9 15h6" stroke="#333" stroke-width="1.5"/></svg></div><strong>640+</strong><span>Factory In Worldwide</span></div>
  <div class="stat" style="left:982px"><div class="ring"><svg width="34" height="34" viewBox="0 0 24 24"><path d="M4 20L14 10M16 4l4 4-3 3-4-4zM4 4l16 16M4 4h4v4" stroke="#333" stroke-width="1.5" fill="none"/></svg></div><strong>3250+</strong><span>Projects Completed</span></div>
</section>

<section class="sec services" role="img" aria-label="Faded photo of a desk with a laptop behind the services overview">
  <h2>Our Services</h2>
  <div class="intro">We have built an enviable reputation in consumer goods, heavy industry, high-tech, manufacturing, medical, recreational vehicle, and transportation sectors.</div>
  <div class="svc-logo">Brivola IT</div>
  <svg class="diagram" width="1200" height="549" viewBox="0 0 1200 549">
    <g stroke="#6b449b" stroke-width="2.5" fill="none">
      <path d="M481 246V292H300M523 246V336H335M560 246V382H370"/>
      <path d="M719 246V292H900M677 246V336H865M640 246V382H830"/>
      <path d="M600 246V411"/>
      <path d="M470 246H730"/>
    </g>
    <g fill="#fff" stroke="#6b449b" stroke-width="2.5">
      <circle cx="292" cy="292" r="6"/><circle cx="327" cy="336" r="6"/><circle cx="362" cy="382" r="6"/>
      <circle cx="908" cy="292" r="6"/><circle cx="873" cy="336" r="6"/><circle cx="838" cy="382" r="6"/>
      <circle cx="600" cy="419" r="6"/>
    </g>
  </svg>
  <div class="svc" style="left:69px;top:279px">Financial Analysis</div>
  <div class="svc" style="left:90px;top:323px">Business Consulting</div>
  <div class="svc" style="left:162px;top:369px">Market research</div>
  <div class="svc" style="left:926px;top:279px">Investment Planning</div>
  <div class="svc" style="left:889px;top:323px">Risk Management</div>
  <div class="svc" style="left:854px;top:369px">Market research</div>
  <div class="svc" style="left:528px;top:440px">Industrial Services</div>
</section>

<section class="sec jobs">
  <h2 style="left:60px">Featured jobs</h2>
  <article class="card" style="left:60px">
    <div class="img" role="img" aria-label="Photo of a hand signing a document" style="background:linear-gradient(135deg,#4a3f38,#a59a90)"><div class="date">Nov<b>23</b></div></div>
    <h3>We travel to you</h3>
    <div class="meta"><span>◷ 3:24 am</span><span>▭ Wednesday</span></div>
    <p>Ready for a vacation? Picture this. You work from home – then one day, a deal comes through. It is the breakthrough you have been....</p>
    <a class="more">Read More &gt;&gt;</a>
  </article>
  <article class="card" style="left:329px">
    <div class="img" role="img" aria-label="Photo of a small team meeting in an office" style="background:linear-gradient(135deg,#8e8a84,#d8d2ca 50%,#3d4a5e)"><div class="date">Nov<b>23</b></div></div>
    <h3>Certified Legal Services</h3>
    <div class="meta"><span>◷ 3:24 am</span><span>▭ Wednesday</span></div>
    <p>A Few Things Are Required For Notary: I.D.: Every signer must show valid (not expired) photo identification. All identification must contain a photo, a physical...</p>
    <a class="more">Read More &gt;&gt;</a>
  </article>
  <div class="faq">
    <h2>FAQ</h2>
    <ul>
      <li><b>+</b>What is Notarisation?</li>
      <li><b>+</b>What is a signing agent?</li>
      <li><b>+</b>Do I need an appointment?</li>
      <li><b>+</b>Why do I need to bring proof of identity and proof of address?</li>
      <li><b>+</b>How much will it cost?</li>
      <li><b>+</b>Where do you provide your services?</li>
      <li><b>+</b>What documents do you notarise?</li>
    </ul>
  </div>
</section>

<section class="sec consult">
  <div class="img" role="img" aria-label="Photo of people working at computers in an office"></div>
  <div class="adviser">
    <h2>Find Adviser</h2>
    <p>Would you like to speak to one of our financial advisers over the phone? Just submit your details and we'll be in touch shortly. You can also e-mail us for any further concern.</p>
    <div class="hours">Monday to Friday : 8AM to 8PM<br>Saturtday : 9AM to 11AM<br>Sunday &amp; Holidays : Closed</div>
  </div>
  <div class="form">
    <h2>Get a Free Consultation</h2>
    <div class="field" style="left:63px;top:118px;width:258px;height:45px">Your Name</div>
    <div class="field" style="left:334px;top:118px;width:226px;height:45px">Your Email</div>
    <div class="field" style="left:63px;top:171px;width:258px;height:46px">Phone</div>
    <div class="field" style="left:334px;top:171px;width:226px;height:46px">Saving &amp; Investing</div>
    <div class="field" style="left:63px;top:226px;width:497px;height:97px">Other Details</div>
    <div class="btn">Find Your Advisor</div>
  </div>
</section>

<section class="sec partners">
  <span>Norvik</span><span>Halden Grid</span><span><i></i>Veltra</span><span><i></i>Ostmark</span><span>Lumaro</span>
</section>

<footer class="sec footer">
  <div class="col" style="left:60px;width:250px">
    <div class="brandf">Brivola IT</div>
    <p style="margin-top:22px">Over 24 years experience and of the international user standards and technological works changes and industrial systems, we dedicated to provide the best and economical.</p>
    <div class="socials"><i></i><i></i><i></i><i></i><i></i></div>
  </div>
  <div class="col" style="left:359px">
    <h4>SERVICES</h4>
    <ul><li>Chemical Research</li><li>Material Science</li><li>Petroleum and Gas</li><li>Mechanical Engineering</li><li>Agriculture Processing</li><li>Power and Energy</li></ul>
  </div>
  <div class="col" style="left:615px;width:250px">
    <h4>RECENT NEWS</h4>
    <div class="news"><div class="thumb" role="img" aria-label="News photo of a lit interior" style="background:linear-gradient(135deg,#5a3a22,#c98a45)"></div><span>Our New Office Is A<br>Space Where..</span></div>
    <div class="news" style="margin-top:44px"><div class="thumb" role="img" aria-label="News photo of a coastline" style="background:linear-gradient(135deg,#2d7bb0,#a6d0e8)"></div><span>Start A Career And We<br>Help...</span></div>
  </div>
  <div class="col" style="left:891px;width:260px">
    <h4>SUBSCRIBE US</h4>
    <p style="margin-top:14px">Subscribe to our newsletter!</p>
    <div class="sub"><div></div><b><svg width="16" height="16" viewBox="0 0 24 24"><path d="M2 12l20-9-7 19-3-8z" fill="#fff"/></svg></b></div>
    <p style="margin-top:10px;font-size:12px">We don't do spam and Your mail id very confidential.</p>
    <div class="socials plain"><i></i><i></i><i></i><i></i><i></i></div>
  </div>
</footer>

<div class="sec bottom">
  <span>Copyright © 2017 Brivola IT All rights reserved</span>
  <nav><span>HOME</span><span>SERVICES</span><span>TERM &amp; CONDITION</span><span>PRIVACY POLICY</span><span>CONTACT US</span></nav>
</div>

</body>
</html>
```